Vantor Medica Innovative Business Card

Stunning business card. Background will be black. Letters in gold. Modern yet simple design that is attention grabbing. QR code leading to site. Attractive primarily to males ages 30 to 50 but also to females in same age range looking for beauty and mental health products

Target Market(s)

Males in the 30-50 age demographics

Industry/Entity Type

Pharmaceuticals selling erectile dysfunction and mens health medications

Contact Information for Business Card

www.vantormedica.example; (775) BUY-KELO; info@vantormedica.example

Colors
FFC000
F8CF3A
FAE287
FDF2CF
FEFAEE

Requirements
Must have
• Black business card with gold letters.
Nice to have
• perhaps just the logo or the "R" icon by itself on one side
Should not have
• too much content so it does not look busy

```html
<!DOCTYPE html>
<html lang="en">
<head>
<meta charset="utf-8">
<title>Vantor Medica – Business Card</title>
<link rel="stylesheet" href="https://fonts.googleapis.com/css2?family=Barlow+Condensed:wght@500;600&display=swap">
<style>
  :root {
    --stage: #464b45;
    --card: #0c0f10;
    --gold: #e3c13a;
    --gold-deep: #c9a21c;
    --gold-light: #e8e56e;
    --gold-mid: #d8aa18;
    --gold-sage: #c8c45e;
    --gold-dark: #b8960e;
  }
  * { margin: 0; padding: 0; box-sizing: border-box; }
  html, body {
    width: 1200px; height: 1105px; overflow: hidden;
    background: var(--stage);
    font-family: "Barlow Condensed", "Arial Narrow", sans-serif;
  }
  .canvas { position: relative; width: 1200px; height: 1105px; }
  .card {
    position: absolute;
    background: var(--card);
    box-shadow: 22px 24px 26px rgba(0,0,0,0.55);
    overflow: hidden;
  }
  .card--front { left: 50px; top: 33px; width: 880px; height: 491px; }
  .card--back  { left: 261px; top: 561px; width: 834px; height: 466px; }

  .brand-name {
    color: var(--gold);
    font-weight: 600;
    white-space: nowrap;
    line-height: 1;
  }
  .card--front .brand-name {
    position: absolute; left: 82px; top: 184px;
    font-size: 40px; letter-spacing: 0.5px;
  }

  .contact-list {
    position: absolute; left: 425px; top: 132px;
    list-style: none;
  }
  .contact-item {
    display: flex; align-items: center;
    height: 49px;
    color: var(--gold);
    font-size: 35px; font-weight: 500;
    letter-spacing: 0.3px;
    white-space: nowrap;
  }
  .contact-icon { width: 34px; height: 34px; margin-right: 10px; flex: none; }

  .gold-band {
    position: absolute; left: 0; right: 0; top: 356px; bottom: 0;
    background:
      linear-gradient(180deg, rgba(12,15,16,0.85) 0%, rgba(12,15,16,0) 45%),
      linear-gradient(90deg, var(--gold-deep) 0%, var(--gold-light) 25%, var(--gold-mid) 42%, var(--gold-sage) 72%, var(--gold-dark) 100%);
  }

  .back-mark {
    position: absolute; left: 50%; top: 108px;
    width: 124px; height: 124px; margin-left: -62px;
    border: 14px solid var(--gold);
    border-radius: 50%;
  }
  .card--back .brand-name {
    position: absolute; left: 0; right: 0; top: 262px;
    text-align: center;
    font-size: 96px; letter-spacing: 1px;
  }
</style>
</head>
<body>
<main class="canvas">

  <section class="card card--front" aria-label="Business card front">
    <div class="gold-band" role="img" aria-label="Decorative gold wave band along the bottom of the card"></div>

    <p class="brand-name">Vantor Medica</p>

    <ul class="contact-list">
      <li class="contact-item">
        <svg class="contact-icon" viewBox="0 0 34 34" aria-hidden="true" fill="none" stroke="var(--gold)" stroke-width="1.6">
          <circle cx="17" cy="17" r="14"/>
          <ellipse cx="17" cy="17" rx="6" ry="14"/>
          <line x1="17" y1="3" x2="17" y2="31"/>
          <line x1="3" y1="17" x2="31" y2="17"/>
          <path d="M6 9.5h22M6 24.5h22"/>
        </svg>
        <span>www.vantormedica.example</span>
      </li>
      <li class="contact-item">
        <svg class="contact-icon" viewBox="0 0 34 34" aria-hidden="true">
          <rect x="1" y="8" width="32" height="20" fill="var(--gold)"/>
          <path d="M2 9 L17 20 L32 9 M2 27 L13 17 M32 27 L21 17" fill="none" stroke="var(--card)" stroke-width="1.8"/>
        </svg>
        <span>info@vantormedica.example</span>
      </li>
      <li class="contact-item">
        <svg class="contact-icon" viewBox="0 0 34 34" aria-hidden="true">
          <path fill="var(--gold)" d="M24 6 C29 4 33 6 33 9 C33 11 30 11 28 10 C24 10 18 14 14 20 C11 24 10 28 11 30 C11 33 7 33 5 31 C3 27 6 19 11 14 C15 10 19 7 24 6 Z"/>
        </svg>
        <span>(775) BUY-KELO</span>
      </li>
    </ul>
  </section>

  <section class="card card--back" aria-label="Business card back">
    <div class="back-mark" aria-hidden="true"></div>
    <p class="brand-name">Vantor Medica</p>
  </section>

</main>
</body>
</html>
```